Business Card Design - Furniture Retail

Open to both Single or double sided design

We are launching a online ecommerce store that sells Scandinavian/Danish style of furniture in Australia.

We aspire to provide stylish but classic and designers' selection of furniture to the Australia public at affordable price. For the style of the furniture we are selling, please see the following links:

https://www.boxlyshare.com/sh/qrk7vz2mwpl04tn/BBXTpeLr3h52Kd7nWqYzRsGmu?dl=0

The style of the design we are looking for is clean, simple that look Scandinavian/Danish but yet it is timeless classic.

Aspiring Design
http://www.hallwick.com
http://brenlowe.com.au/
http://kolvo.furniture/
http://www.tipo.com/
Updates

Please display the card on normal angle for both front and back instead of funny angle. Please keep it display when displaying the design of the business cards so that we can focus on the designs rather than being confused by the unnecessary stuffs like the hands or background

I think there is already enough curve line on the logo itself so anything extra of the curve on the business card would be really unnecessary. Please avoid using any of the extra curve line on the business card, other than the logo itself. Thanks

Regular card and give them a matt celloglaze to create texture on card that makes it looked luxury and expensive.

Please display design on normal angle! Please only use white colour in the background (not the business card but the referring to the submission) rather than anything fancy so that we can focus on the design.

Target Market(s)

High end market consumers who are financially capable and who has good taste and appreciate good design

aged between 28 - 45 white collars professional/businessmen who live in metropolitan areas

Industry/Entity Type

Business

Font styles to use
Serif
Sans Serif

Requirements
Must have
• Regular card and give them a matt celloglaze to create texture on card that makes it looked luxury and expensive.

Please use the logo from the uploaded files

Company Name: Miles Orveda
Name: Peter Holm
Phone: +614 27 505 316
Website: www.milesorveda.com.au
Email: peter@milesorveda.com.au
Nice to have
• Colour is not limited to black and white
Should not have
• The concept photos of the furniture should NOT be used in the FRONT page of the business card.

```html
<!DOCTYPE html>
<html lang="en">
<head>
<meta charset="utf-8">
<title>Miles Orveda — Business Card</title>
<link rel="stylesheet" href="https://fonts.googleapis.com/css2?family=Marcellus&family=Sorts+Mill+Goudy&display=swap">
<style>
  :root {
    --card-bg: #ffffff;
    --ink: #111111;
    --gold: #9a6b12;
  }
  * { margin: 0; padding: 0; box-sizing: border-box; }
  html, body {
    width: 1200px;
    height: 741px;
    overflow: hidden;
    background: var(--card-bg);
  }
  .card {
    position: relative;
    width: 1200px;
    height: 741px;
    background: var(--card-bg);
    color: var(--ink);
  }
  .brand {
    position: absolute;
    top: 92px;
    right: 75px;
    font-family: "Marcellus", serif;
    font-size: 60px;
    line-height: 1;
    letter-spacing: 1px;
    text-transform: uppercase;
    color: var(--ink);
    white-space: nowrap;
  }
  .holder-name {
    position: absolute;
    left: 90px;
    top: 352px;
    font-family: "Marcellus", serif;
    font-size: 70px;
    line-height: 1;
    letter-spacing: 2px;
    color: var(--gold);
  }
  .contact {
    position: absolute;
    left: 78px;
    top: 518px;
    list-style: none;
    font-family: "Sorts Mill Goudy", serif;
    font-size: 36px;
    line-height: 48px;
    color: var(--ink);
  }
  .contact .label-wide { letter-spacing: 5px; }
</style>
</head>
<body>
  <main class="card">
    <div class="brand">Miles Orveda</div>
    <h1 class="holder-name">Peter Holm</h1>
    <ul class="contact">
      <li class="contact-phone">phone: +614 27 505 316</li>
      <li class="contact-web">website: www.milesorveda.com.au</li>
      <li class="contact-email"><span class="label-wide">email:</span> peter@milesorveda.com.au</li>
    </ul>
  </main>
</body>
</html>
```